Velmor Integrated Company Profile

We are looking for a new design for our company profile. We need two output formats. A PDF version to use as a soft copy. Another version is needed for printing.

We are seeking an A4 profile based on the same text content of our old one. Some new content will be provided once the graphics are confirmed.

Attached is our old profile. Please give us a newer design. Once design is confirmed we will provide the new content to use.
I am available for any answers or feedback.

Target Market(s)

This is used for introducing our company to the customers.
We are also seeking investors, so they might be considered

Industry/Entity Type

Information Technology

Requirements
Must have
• Info-graphics based on the data in old profile
• Some info-graphics about number of orders, customers and sales volume
• We have two websites for selling online; nilecallkit.com and dunelinkgear.com. We need to include them in a way or another in the profile. Their logos are in the attached files.
Nice to have
• Any new suggestions about content to include in the profile will be welcomed

```html
<!DOCTYPE html>
<html lang="en">
<head>
<meta charset="utf-8">
<title>Velmor Integrated – Company Profile, Page 1</title>
<link rel="stylesheet" href="https://fonts.googleapis.com/css2?family=Oswald:wght@300;400&family=Questrial&display=swap">
<style>
  :root {
    --navy: #14305a;
    --navy-deep: #0c2246;
    --band-blue: #2a5b8e;
    --orange: #f7941d;
    --ink: #1a1a1a;
    --white: #ffffff;
    --metal-light: #f4f4f5;
    --metal-mid: #d9dadc;
    --metal-dark: #c4c6c9;
  }
  html, body {
    margin: 0;
    padding: 0;
    width: 848px;
    height: 1200px;
    overflow: hidden;
  }
  .page {
    position: relative;
    width: 848px;
    height: 1200px;
    overflow: hidden;
    background:
      repeating-linear-gradient(180deg, rgba(255,255,255,0.18) 0 1px, rgba(0,0,0,0.025) 1px 3px),
      radial-gradient(ellipse 70% 55% at 52% 50%, var(--metal-light) 0%, var(--metal-mid) 70%, var(--metal-dark) 100%);
  }
  .header-bands, .footer-bands {
    position: absolute;
    left: 0;
    width: 848px;
  }
  .header-bands { top: 24px; height: 58px; }
  .footer-bands { top: 1142px; height: 22px; }
  .section-title {
    position: absolute;
    top: 34px;
    left: 21px;
    margin: 0;
    font-family: "Oswald", sans-serif;
    font-weight: 300;
    font-size: 27px;
    letter-spacing: 4px;
    color: var(--white);
    line-height: 1;
  }
  .page-number {
    position: absolute;
    top: 35px;
    right: 21px;
    margin: 0;
    font-family: "Oswald", sans-serif;
    font-weight: 400;
    font-size: 27px;
    letter-spacing: 1px;
    color: var(--white);
    line-height: 1;
  }
  .ceo-letter {
    position: absolute;
    top: 326px;
    left: 76px;
    width: 698px;
    font-family: "Questrial", sans-serif;
    font-size: 18.6px;
    line-height: 24.2px;
    color: var(--ink);
  }
  .ceo-letter p {
    margin: 0 0 17.6px;
    text-align: justify;
    hyphens: auto;
  }
  .ceo-letter .thanks { margin-bottom: 13px; text-align: left; }
  .ceo-letter .signature { text-align: left; margin: 0; }
  .brand-mark {
    position: absolute;
    top: 1118px;
    left: 0;
    width: 848px;
    display: flex;
    justify-content: center;
    align-items: center;
    gap: 10px;
  }
  .brand-square {
    width: 26px;
    height: 26px;
    background: var(--navy);
  }
  .brand-name {
    font-family: "Questrial", sans-serif;
    font-size: 34px;
    letter-spacing: 5px;
    color: var(--orange);
    line-height: 1;
  }
</style>
</head>
<body>
<main class="page">
  <svg class="header-bands" viewBox="0 0 848 58" aria-hidden="true">
    <defs>
      <linearGradient id="navyBand" x1="0" y1="0" x2="1" y2="0">
        <stop offset="0" stop-color="var(--navy-deep)"/>
        <stop offset="1" stop-color="var(--navy)"/>
      </linearGradient>
    </defs>
    <polygon points="0,0 672,0 648,58 0,58" fill="url(#navyBand)"/>
    <polygon points="678,0 848,0 848,58 656,58" fill="var(--orange)"/>
  </svg>
  <h1 class="section-title">COMPANY PROFILE</h1>
  <p class="page-number">PAGE 1</p>

  <article class="ceo-letter">
    <p>We find it our continuous responsibility to make sure that our customers are running the latest, most stable and most effective Unified Communications technology and products. At the same time, we exert our best for them to maintain the highest adoption and ROI of their UC networks investments.</p>
    <p>Our experienced highly innovative team is our capital to enable Velmor maintain the customer confidence we gained along our history in our service level and technical excellence.</p>
    <p>We are proud to lead the change in B2B IT services concepts in the MENA region. We know that customers’ daily B2C experience raised their expectation to a real time information flow of their orders and services. With our new operation model and latest customer interactive technologies we started to implement in 2016; we enabled our customers to request, receive and manage services, manage purchased assets and orders in cooperation with Velmor team in real time. We know our customer time is very valuable and we care to make the most of it.</p>
    <p class="thanks">Thanks for being our customer ☺</p>
    <p class="signature">Karim Halden<br>Chairman, Co-Founder &amp; CEO</p>
  </article>

  <svg class="footer-bands" viewBox="0 0 848 22" aria-hidden="true">
    <polygon points="0,0 321,0 332,22 0,22" fill="var(--band-blue)"/>
    <polygon points="552,0 848,0 848,22 539,22" fill="var(--orange)"/>
  </svg>

  <div class="brand-mark">
    <span class="brand-square"></span>
    <span class="brand-name">VELMOR</span>
  </div>
</main>
</body>
</html>
```